women's junior contemporary apparel company.
We are looking for a business card that represents our urban design aesthetic. We would like to keep it simple and modern/contemporary.
the name of the company is 'v-lanza'.

we've attached a font style but you are not limited solely to use this font. All suggestions are welcomed.

```html
<!DOCTYPE html>
<html lang="en">
<head>
<meta charset="utf-8">
<title>v-lanza business card</title>
<link rel="stylesheet" href="https://fonts.googleapis.com/css2?family=Oswald:wght@500;600&family=Cinzel:wght@400&display=swap">
<style>
  :root {
    --stage: #3a3a3c;
    --quilt-light: #fbfbfb;
    --quilt-mid: #e4e4e6;
    --quilt-shade: #c9c9cd;
    --cream: #f6f2cf;
    --cream-deep: #e9e0a8;
    --gold: #d8b62a;
    --gold-deep: #b8941a;
    --panel-gold: #eccb75;
    --panel-gold-deep: #e2b957;
    --panel-text: #fffaf0;
  }
  html, body {
    margin: 0;
    padding: 0;
    width: 1200px;
    height: 1200px;
    overflow: hidden;
    background: var(--stage);
  }
  .sheet {
    position: relative;
    width: 1200px;
    height: 1200px;
  }
  .card {
    position: absolute;
    left: 170px;
    width: 860px;
    height: 491px;
    overflow: hidden;
    box-shadow: 0 10px 30px rgba(0,0,0,0.35);
  }
  .card--back { top: 80px; }
  .card--front { top: 630px; }

  .card__pattern {
    position: absolute;
    inset: 0;
    width: 100%;
    height: 100%;
  }
  .card--back .card__pattern {
    background: radial-gradient(ellipse at 50% 50%, var(--cream) 0%, var(--cream) 55%, var(--cream-deep) 100%);
  }
  .card--front .card__pattern {
    background: radial-gradient(ellipse at 50% 40%, var(--quilt-light) 0%, var(--quilt-mid) 70%, var(--quilt-shade) 100%);
  }

  .details-panel {
    position: absolute;
    left: 215px;
    top: 120px;
    width: 480px;
    height: 270px;
    background: linear-gradient(160deg, var(--panel-gold) 0%, var(--panel-gold-deep) 100%);
    box-sizing: border-box;
    padding: 52px 40px 0 28px;
  }
  .details-row {
    display: flex;
    align-items: baseline;
    gap: 14px;
    height: 64px;
    font-family: "Cinzel", serif;
    font-size: 26px;
    color: var(--panel-text);
    letter-spacing: 0.04em;
  }
  .details-row__line {
    flex: 1;
    border-bottom: 2px dashed rgba(255,250,240,0.75);
    transform: translateY(-6px);
  }

  .brand {
    position: absolute;
    left: 0;
    right: 0;
    top: 150px;
    text-align: center;
  }
  .brand__name {
    font-family: "Oswald", sans-serif;
    font-weight: 600;
    font-size: 128px;
    line-height: 1;
    color: var(--gold);
    letter-spacing: 0.02em;
  }
  .brand__tagline {
    margin-top: 22px;
    font-family: "Oswald", sans-serif;
    font-weight: 500;
    font-size: 24px;
    color: var(--gold-deep);
    letter-spacing: 0.08em;
  }
</style>
</head>
<body>
  <main class="sheet">
    <section class="card card--back">
      <div class="card__pattern" role="img" aria-label="Embossed gold swirl and dot ornament pattern on cream"></div>
      <div class="details-panel">
        <div class="details-row"><span>Name</span><span class="details-row__line"></span></div>
        <div class="details-row"><span>Tel</span><span class="details-row__line"></span></div>
        <div class="details-row"><span>Address</span><span class="details-row__line"></span></div>
      </div>
    </section>

    <section class="card card--front">
      <div class="card__pattern" role="img" aria-label="White quilted diamond upholstery pattern with pearl buttons"></div>
      <div class="brand">
        <div class="brand__name">v-lanza</div>
        <div class="brand__tagline">WOMEN'S APPAREL</div>
      </div>
    </section>
  </main>
</body>
</html>
```